Book Cover Design for Millennial

I need a book cover design for my book Sunward Ledger. The subtitle of the book is Seven Quiet Steps Toward Steady Ground at Work.

I'm a career coach who helps millennial career professionals. I myself am a millennial but on the older end (34). I've dealt and been through most of the challenges millennials are facing as career professionals and I wrote this book with the thought of providing guidance and aid to getting past those challenges and shedding light on fundamental habits and practices that will help them excel in their careers. In addition, the book will help them prepare millennials for our turn as the leaders, managers, etc moving forward in corporate America. The final design should have the main title of the book in it as the focal point but not the subtitle. I want the cover to communicate something NEW, Bold, Youthful, non-traditional. I want it to stick out while still maintaining a sleek and Professional look.
Updates

Hello, Designers! I want to thank you all for your submissions! The work is amazing and I greatly appreciate it. If you would I want to help out in this process by adding a few updates based on the submissions I have seen. The concept I think that is coming close to hitting the mark is Bramble Forja. What I would like to see changed about the concept is the following: Change the outfits to be more Millennial Career Professional. I have attached some ideas to the brief. I want to replace this picture with one of multiple millennials anywhere from 3 and up. I would like the pic to have diversity in it representing most races of people in the USA. I would like my name beneath sunward ledger. I'm not a known author yet so having my name that big my distract from the title of the book. Can we make the title a little bigger and so far I like the background.Thanks, DP Added Friday, September 30, 2016

Target Market(s)

Millennial Career Professionals (18 - 34 age group)

Industry/Entity Type

Life Coaching

Logo Text

Sunward Ledger

Requirements
Must have
• communicate something NEW, Bold, Youthful, non-traditional. I want it to stick out while still maintaining a sleek and Professional look.
Nice to have
• something that goes with my brand
• http://www.doranpelwick.com
Should not have
• Nothing 3D or a logo that is hard to read when placed on stationeries, business cards etc

```html
<!DOCTYPE html>
<html lang="en">
<head>
<meta charset="utf-8">
<title>Sunward Ledger — Book Cover</title>
<link rel="stylesheet" href="https://fonts.googleapis.com/css2?family=Anton&family=Archivo+Black&family=Dancing+Script:wght@700&display=swap">
<style>
  :root {
    --mint: #96fde0;
    --magenta: #ef0ddc;
    --ink: #000000;
    --paper: #ffffff;
    --skin-warm: #c99877;
    --shirt-light: #e9ecdc;
    --shirt-green: #a5b46a;
  }
  html, body {
    margin: 0;
    padding: 0;
    overflow: hidden;
    background: var(--paper);
  }
  .cover {
    position: relative;
    width: 934px;
    height: 1200px;
    overflow: hidden;
    background: var(--mint);
  }
  .cover-backdrop {
    position: absolute;
    inset: 0;
    width: 934px;
    height: 1200px;
  }
  .group-photo {
    position: absolute;
    left: 318px;
    top: 800px;
    width: 616px;
    height: 400px;
    background: linear-gradient(100deg, var(--skin-warm) 0%, var(--shirt-light) 45%, var(--shirt-green) 100%);
  }
  .title-main {
    position: absolute;
    left: 60px;
    top: 140px;
    margin: 0;
    font-family: "Anton", "Oswald", sans-serif;
    font-size: 124px;
    line-height: 1;
    letter-spacing: -2px;
    color: var(--ink);
    -webkit-text-stroke: 8px var(--paper);
    paint-order: stroke fill;
    text-transform: uppercase;
    white-space: nowrap;
  }
  .title-script {
    position: absolute;
    left: 122px;
    top: 258px;
    margin: 0;
    font-family: "Dancing Script", cursive;
    font-weight: 700;
    font-size: 172px;
    line-height: 1;
    color: var(--ink);
    -webkit-text-stroke: 8px var(--paper);
    paint-order: stroke fill;
    white-space: nowrap;
  }
  .subtitle {
    position: absolute;
    left: 96px;
    top: 466px;
    margin: 0;
    font-family: "Archivo Black", "Arial Black", sans-serif;
    font-size: 37px;
    line-height: 1.2;
    color: var(--ink);
    white-space: nowrap;
  }
  .byline {
    position: absolute;
    left: 106px;
    top: 856px;
    margin: 0;
    font-family: "Anton", "Oswald", sans-serif;
    font-size: 66px;
    line-height: 1.05;
    letter-spacing: -1px;
    color: var(--ink);
    -webkit-text-stroke: 6px var(--paper);
    paint-order: stroke fill;
    white-space: nowrap;
  }
</style>
</head>
<body>
  <main class="cover">
    <svg class="cover-backdrop" viewBox="0 0 934 1200" aria-hidden="true">
      <polygon points="0,0 934,1200 0,1200" fill="var(--magenta)"/>
    </svg>

    <div class="group-photo" role="img" aria-label="Photograph of a diverse group of young professionals standing together, facing the viewer"></div>

    <h1 class="title-main">Sunward</h1>
    <p class="title-script">Ledger</p>

    <p class="subtitle">Seven Quiet Steps Toward<br>Steady Ground at Work.</p>

    <p class="byline">by:<br>doran pelwick</p>
  </main>
</body>
</html>
```